Cover für den Roman Marlene betritt die Bühne
Zielgruppe
Autorin einer belletristischen Erzählung über die Kunst der Moderne. Das Buch richtet sich an Leser die sich für Moderne Kunst interessieren.
Aufgabenstellung
Gesucht wird ein sehr zeitgemäßes und auffallendes Design, auch gerne mit einer starken Hintergrundfarbe. Der Leser soll auf den ersten Blick erkennen können, dass es hier um Kunst geht (Lorenz Aubach, Tarnowski, Ferrandi Hadley, etc). Bitte unbedingt alle Lizenzrechte abklären und keine Originalwerke verwenden.
Eine Idee wäre einen Bezug zu "Marlene und der Barastides" herzustellen. (Vielzitiertes Thema in der Kunstgeschichte, Marlene schlägt dem Feldherrn Barastides den Kopf ab und befreit ihr Volk.)
Das Design sollte aber trotzdem nett und nicht gruselig sein.
Ganz wichtig keine nackte Marlene. Sie ist stark und emanzipiert sich!
Text auf der Vorderseite:
Olga Mertelhuber
Marlene betritt die Bühne
Erzählung über die Kunst der Moderne
Text auf der Rückseite:
kurze Inhaltsangabe
Das Cover soll für ein Taschenbuch als auch ein e-book funktionieren

```html
<!DOCTYPE html>
<html lang="de">
<head>
<meta charset="utf-8">
<title>Marlene betritt die Bühne – Rückseite</title>
<link href="https://fonts.googleapis.com/css2?family=Anton&family=Tinos&display=swap" rel="stylesheet">
<style>
  :root {
    --paper-light: #e6ecee;
    --paper-mid: #c9d5d9;
    --accent-red: #9a0d06;
    --title-band: #58595b;
    --title-text: #ffffff;
    --body-text: #111111;
    --sketch-light: #b9c3c6;
    --sketch-dark: #3a3c3e;
  }
  html, body {
    margin: 0;
    padding: 0;
    overflow: hidden;
    background: #ffffff;
  }
  .back-cover {
    position: relative;
    width: 840px;
    height: 1200px;
    overflow: hidden;
    background:
      radial-gradient(ellipse at 30% 20%, var(--paper-light) 0%, transparent 55%),
      radial-gradient(ellipse at 70% 70%, #dde5e8 0%, transparent 60%),
      linear-gradient(180deg, var(--paper-mid) 0%, var(--paper-light) 45%, #d4dde0 100%);
  }
  .decor {
    position: absolute;
    inset: 0;
    width: 840px;
    height: 1200px;
  }
  .title-band {
    position: absolute;
    left: 0;
    top: 262px;
    width: 763px;
    height: 76px;
    background: var(--title-band);
  }
  .title {
    position: absolute;
    right: 8px;
    top: 2px;
    margin: 0;
    font-family: "Anton", "Impact", sans-serif;
    font-weight: 400;
    font-size: 54px;
    line-height: 72px;
    color: var(--title-text);
    white-space: nowrap;
    letter-spacing: 0.5px;
  }
  .synopsis {
    position: absolute;
    left: 100px;
    top: 357px;
    width: 640px;
    margin: 0;
    font-family: "Tinos", "Times New Roman", serif;
    font-size: 24px;
    line-height: 38px;
    text-align: center;
    white-space: nowrap;
    color: var(--body-text);
  }
</style>
</head>
<body>
  <main class="back-cover">
    <svg class="decor" viewBox="0 0 840 1200" xmlns="http://www.w3.org/2000/svg">
      <defs>
        <linearGradient id="sketch-tone" x1="0" y1="0" x2="1" y2="1">
          <stop offset="0" stop-color="var(--sketch-light)"/>
          <stop offset="0.55" stop-color="#8d9497"/>
          <stop offset="1" stop-color="var(--sketch-dark)"/>
        </linearGradient>
      </defs>
      <polygon class="red-strip" points="760,0 840,0 840,1200 773,1200 773,256 760,256" fill="var(--accent-red)"/>
      <polygon class="sketch-sheet" role="img" aria-label="Bleistiftskizze eines Männerkopfes auf schräg gelegtem Papier"
               points="605,848 840,925 840,1200 512,1200" fill="url(#sketch-tone)" opacity="0.9"/>
    </svg>

    <header class="title-band">
      <h1 class="title">Marlene betritt die Bühne</h1>
    </header>

    <p class="synopsis">
      Marlene und Valentin begegnen sich unverhofft<br>
      in einem Museum und sprechen lange über die<br>
      Kunst der Moderne. So lernt der Leser nebenbei<br>
      vieles über die Kunstgeschichte seit etwa 1900.<br>
      Warum die Kamera die Malerei verändern musste,<br>
      was die Tube voller Farbe für die Maler im<br>
      Freien bedeutete und weshalb Geräusche auch<br>
      Musik sein können, wird leicht erklärt.<br>
      Zum Schluss macht Marlene ihrem Namen Ehre<br>
      und bringt den besserwisserischen Herrn<br>
      endgültig zum Schweigen. So setzt sich die<br>
      Selbstbestimmung gegen alte Rollenbilder<br>
      durch, ganz wie es die Moderne verlangt.
    </p>
  </main>
</body>
</html>
```